Cryptocurrency Advisor Business Card

Dravelin Consulting Services is my company, which advises many projects in the ICO/Cryptocurrency industry. I'd like to get a sleek, preferably matte black or matte dark blue finish, business card with the company name (and simple logo w/ crypto feel) on one side and while the other side I'd like a small twitter and telegram logo together maybe separated by a / as it's the same, then an email and a phone logo so I can insert those specifics there (no address). Can have name then CEO section too. At the bottom of that section, find a place for more of a job description: ICO Advisor, World Champion Gamer, Esports Award Winner, Quorvane Expert. You can possibly design a simple logo or use something with a crypto twist or background, but nothing too complex. Rounded edges for printing not square.
Updates

Had personal issues taking a few days away from me being able to provide feedback and check designs, etc. Will be more active now finalizing design just needed few days from issue but all is sorted.

Target Market(s)

Cryptocurrency industry

Industry/Entity Type

Management Consulting

Contact Information for Business Card

Font styles to use
Sans Serif

Colors
5c5c5c
474747
757575
9d9d9d
aaaaaa
333333
0355a3

Requirements
Must have
• Refer to Details/Description
Nice to have
Should not have
• Address section

```html
<!DOCTYPE html>
<html lang="en">
<head>
<meta charset="UTF-8">
<title>Dravelin Consulting Services – Business Card</title>
<link href="https://fonts.googleapis.com/css2?family=Oswald:wght@400;500&family=Arimo:wght@400&display=swap" rel="stylesheet">
<style>
  :root {
    --bg: #1c1c1c;
    --card: #232323;
    --card-edge: #2c2c2c;
    --ink: #f2f2f2;
    --silver: #b9b9b9;
    --indigo: #3a35a3;
    --faint: #2b2b2b;
    --rule: #d8d8d8;
  }
  * { margin: 0; padding: 0; box-sizing: border-box; }
  html, body { width: 1200px; height: 1200px; overflow: hidden; background: var(--bg); }
  .canvas { position: relative; width: 1200px; height: 1200px; }
  .card {
    position: absolute; left: 150px; width: 900px; height: 514px;
    background: var(--card); border-radius: 26px; border: 1px solid var(--card-edge);
    overflow: hidden;
  }
  .card--front { top: 66px; }
  .card--back { top: 620px; }

  /* front */
  .front-mark { position: absolute; left: 50%; top: 120px; transform: translateX(-50%); text-align: center; }
  .front-mark .dot { width: 110px; height: 110px; border-radius: 50%; border: 6px solid var(--silver); margin: 0 auto 28px; }
  .wordmark { font-family: "Oswald", sans-serif; font-weight: 500; letter-spacing: 10px; line-height: 1; }
  .front-mark .wordmark { color: var(--silver); font-size: 58px; }
  .tagline { font-family: "Oswald", sans-serif; font-weight: 400; letter-spacing: 4px; text-transform: uppercase; line-height: 1; }
  .front-mark .tagline { color: var(--silver); font-size: 20px; margin-top: 10px; }

  /* back */
  .faint-circle { position: absolute; right: -40px; top: 40px; width: 360px; height: 360px; border-radius: 50%; border: 26px solid var(--faint); }
  .brand-row { position: absolute; left: 60px; top: 50px; display: flex; align-items: center; gap: 24px; }
  .brand-row .dot { width: 100px; height: 100px; border-radius: 50%; border: 6px solid var(--ink); }
  .brand-row .wordmark { color: var(--ink); font-size: 52px; }
  .brand-row .tagline { color: var(--indigo); font-size: 22px; margin-top: 6px; }
  .person { position: absolute; left: 60px; top: 200px; }
  .person .name { font-family: "Oswald", sans-serif; font-size: 38px; color: var(--ink); letter-spacing: 1px; text-transform: uppercase; line-height: 1.1; }
  .person .role { font-family: "Oswald", sans-serif; font-size: 22px; color: var(--indigo); line-height: 1.1; }
  .rule { position: absolute; left: 60px; right: 60px; top: 300px; height: 1px; background: var(--rule); }
  .duties { position: absolute; left: 60px; top: 322px; list-style: none; font-family: "Arimo", sans-serif; font-size: 19px; color: var(--indigo); line-height: 1.35; }
  .contacts { position: absolute; right: 60px; top: 322px; list-style: none; font-family: "Arimo", sans-serif; font-size: 19px; color: var(--ink); }
  .contacts li { display: flex; justify-content: flex-end; align-items: center; gap: 12px; height: 32px; }
  .contacts svg, .contacts .social { width: 18px; height: 18px; flex: none; }
  .contacts .social { border-radius: 50%; background: var(--indigo); }
</style>
</head>
<body>
<div class="canvas">
  <section class="card card--front">
    <div class="front-mark">
      <div class="dot"></div>
      <div class="wordmark">DRAVELIN</div>
      <div class="tagline">Consulting Services</div>
    </div>
  </section>

  <section class="card card--back">
    <div class="faint-circle"></div>
    <div class="brand-row">
      <div class="dot"></div>
      <div>
        <div class="wordmark">DRAVELIN</div>
        <div class="tagline">Consulting Services</div>
      </div>
    </div>
    <div class="person">
      <div class="name">Corin Vale</div>
      <div class="role">CEO</div>
    </div>
    <div class="rule"></div>
    <ul class="duties">
      <li>ICO Advisor</li>
      <li>World Champion Gamer</li>
      <li>Esports Award Winner</li>
      <li>Quorvane Expert</li>
    </ul>
    <ul class="contacts">
      <li>028-555-0193
        <svg viewBox="0 0 24 24" aria-hidden="true"><path fill="#3a35a3" d="M6.6 10.8a15 15 0 006.6 6.6l2.2-2.2a1 1 0 011-.25 11.4 11.4 0 003.6.57 1 1 0 011 1V20a1 1 0 01-1 1A17 17 0 013 4a1 1 0 011-1h3.5a1 1 0 011 1c0 1.25.2 2.45.57 3.6a1 1 0 01-.25 1z"/></svg></li>
      <li>corinvale@dravelinconsulting.com
        <svg viewBox="0 0 24 24" aria-hidden="true"><rect x="2" y="5" width="20" height="14" rx="1" fill="#3a35a3"/><path d="M2 6l10 7 10-7" stroke="#232323" stroke-width="1.6" fill="none"/></svg></li>
      <li>dravelinconsulting <span class="social"></span></li>
      <li>dravelinconsulting <span class="social"></span></li>
    </ul>
  </section>
</div>
</body>
</html>
```